Elegant Financial Planning Business Card

Clear Harbour Wealth Advisory Pty Ltd requires an elegant business card that communicates simplicity, elegance and trust.
Attached card example of 'Dorvane' is very close to what I am looking for. Looking for black and white card.
Update 24/1/16: The attached Dorvane card is almost exactly what I am looking for. Although it is possible that alternative layouts may interest me, it is considerably more likely that I will proceed with a virtual clone of the "Dorvane' example.
Industry/Entity Type
Financial Planning
Contact Information for Business Card
In black font...
Front Details are (layout as per Paula Dorvane card picture):
Line1 - Name: Simon Walsh
Line 2 - Company: Clear Harbour Wealth Advisory Pty Ltd
Line 3 - Address: Marlow Court 3, Level 14, 58 Tennant Road, Bondi Junction NSW
Line 4
- Phone: 178 526
- Email: advice@chwa-example.com.au
- Site: www.chwa-example.com.au
Back details
1/ logo in position and dimensions as per attached layout
2. Bottom left (in smaller writing).
- Authorised Representative No. 517649
- Clear Harbour Wealth Advisory is a corporate authorised representative of Tidewell Capital Partners Pty Ltd
- ABN 47 318 602 154
- AFSL No. 390817

```html
<!DOCTYPE html>
<html lang="en">
<head>
<meta charset="utf-8">
<title>Clear Harbour Wealth Advisory – Business Card</title>
<link rel="stylesheet" href="https://fonts.googleapis.com/css2?family=Playfair+Display:wght@400;700&display=swap">
<style>
  :root {
    --page-bg: #ece9e4;
    --card-bg: #ffffff;
    --ink: #111111;
    --ink-soft: #2a2a2a;
    --card-shadow: rgba(0, 0, 0, 0.14);
  }
  * { margin: 0; padding: 0; box-sizing: border-box; }
  html, body {
    width: 1200px;
    height: 700px;
    overflow: hidden;
    background: var(--page-bg);
  }
  .canvas {
    position: relative;
    width: 1200px;
    height: 700px;
    display: flex;
    align-items: center;
    justify-content: center;
    gap: 60px;
  }
  .card {
    position: relative;
    width: 520px;
    height: 300px;
    background: var(--card-bg);
    box-shadow: 0 6px 18px var(--card-shadow);
    color: var(--ink);
    font-family: "Playfair Display", serif;
  }
  .wordmark {
    position: absolute;
    top: 28px;
    right: 34px;
    text-align: right;
    font-family: "Playfair Display", serif;
    font-weight: 700;
    font-size: 42px;
    line-height: 1.0;
    color: var(--ink);
  }

  /* Front */
  .front-details {
    position: absolute;
    left: 34px;
    bottom: 28px;
  }
  .holder-name {
    font-weight: 700;
    font-size: 21px;
    margin-bottom: 4px;
  }
  .company-name {
    font-size: 9.5px;
    color: var(--ink-soft);
    margin-bottom: 8px;
  }
  .address {
    font-size: 9.5px;
    color: var(--ink-soft);
    margin-bottom: 22px;
  }
  .contact-list { list-style: none; font-size: 9px; color: var(--ink-soft); }
  .contact-item {
    display: flex;
    align-items: center;
    gap: 5px;
    margin-bottom: 3px;
  }
  .contact-icon { width: 9px; height: 9px; flex: none; }
  .website { margin-top: 8px; font-size: 9.5px; color: var(--ink-soft); }

  /* Back */
  .compliance {
    position: absolute;
    left: 34px;
    top: 148px;
    display: flex;
    align-items: flex-start;
    gap: 18px;
  }
  .rep-number {
    font-weight: 700;
    font-size: 13px;
    margin-bottom: 3px;
    white-space: nowrap;
  }
  .disclosure {
    font-size: 7.5px;
    line-height: 1.35;
    width: 210px;
    color: var(--ink-soft);
  }
  .registrations {
    margin-top: 4px;
    font-size: 7.5px;
    line-height: 1.5;
    text-align: right;
    white-space: nowrap;
    color: var(--ink-soft);
  }
</style>
</head>
<body>
<main class="canvas">

  <section class="card card-front" aria-label="Business card front">
    <div class="wordmark">Clear<br>Harbour</div>
    <div class="front-details">
      <p class="holder-name">Simon Walsh</p>
      <p class="company-name">Clear Harbour Wealth Advisory Pty Ltd</p>
      <p class="address">Marlow Court 3, Level 14, 58 Tennant Road, Alderby Heights</p>
      <ul class="contact-list">
        <li class="contact-item">
          <svg class="contact-icon" viewBox="0 0 10 10" aria-hidden="true">
            <circle cx="5" cy="5" r="5" fill="#111"/>
            <path d="M3.2 2.6c.3-.2.6-.1.7.2l.4.8c.1.2 0 .4-.2.5l-.3.2c.3.7.8 1.2 1.5 1.5l.2-.3c.1-.2.3-.3.5-.2l.8.4c.3.1.4.4.2.7l-.3.4c-.3.3-.8.4-1.2.2C4.2 6.5 3.5 5.8 3 4.5c-.2-.4-.1-.9.2-1.2z" fill="#fff"/>
          </svg>
          <span>178 526</span>
        </li>
        <li class="contact-item">
          <svg class="contact-icon" viewBox="0 0 10 10" aria-hidden="true">
            <circle cx="5" cy="5" r="5" fill="#111"/>
            <rect x="2.6" y="3.4" width="4.8" height="3.3" fill="none" stroke="#fff" stroke-width="0.6"/>
            <path d="M2.6 3.4 5 5.3 7.4 3.4" fill="none" stroke="#fff" stroke-width="0.6"/>
          </svg>
          <span>advice@chwa-example.com.au</span>
        </li>
      </ul>
      <p class="website">www.chwa-example.com.au</p>
    </div>
  </section>

  <section class="card card-back" aria-label="Business card back">
    <div class="wordmark">Clear<br>Harbour</div>
    <div class="compliance">
      <div>
        <p class="rep-number">Authorised Representative No. 517649</p>
        <p class="disclosure">Clear Harbour Wealth Advisory is a corporate authorised representative of Tidewell Capital Partners Pty Ltd</p>
      </div>
      <div class="registrations">
        <p>ABN 47 318 602 154</p>
        <p>AFSL No. 390817</p>
      </div>
    </div>
  </section>

</main>
</body>
</html>
```